Climb the Marlow

Need a Postcard for Lumen Harbor Card Service Campaign that is flexible and dates and times can be changed as needed. create an invitation section.."You're Invited" to a workshop...Time, Date, Place is what needs to be changeable on the Korvel Lantis version for us to log in and order on an as needed basis. Will this be loaded onto our Korvel Lantis Account to change the info as we mail? Must be formatted properly for Lumen Harbor Card Service in United States. Postcard size will be 9" Wide X 6" high. The focus is on the word MARLOW....

```html
<!DOCTYPE html>
<html lang="en">
<head>
<meta charset="utf-8">
<title>Climb the Marlow – Workshop Postcard</title>
<link rel="stylesheet" href="https://fonts.googleapis.com/css2?family=Open+Sans:ital,wght@0,300;0,400;0,600;0,700;0,800;1,400&display=swap">
<style>
  :root {
    --ink: #111111;
    --paper: #ffffff;
    --mint: #74fbb1;
    --mint-pale: #b8fdd8;
    --coral: #ff3560;
    --brand-violet: #6b68d9;
  }
  html, body {
    margin: 0;
    padding: 0;
    overflow: hidden;
    background: var(--paper);
  }
  .postcard {
    position: relative;
    width: 927px;
    height: 1200px;
    overflow: hidden;
    background: var(--paper);
    color: var(--ink);
    font-family: "Open Sans", Arial, sans-serif;
  }
  .postcard > * { position: absolute; margin: 0; }

  .swoosh-band { left: 0; top: 0; width: 927px; height: 600px; }

  .headline {
    left: 58px; top: 22px;
    font-size: 53px; font-weight: 300; letter-spacing: 1px; line-height: 1.1;
  }
  .headline strong { font-weight: 800; letter-spacing: 0; }

  .subhead {
    left: 62px; top: 89px;
    font-size: 20px; font-weight: 400; letter-spacing: 1.2px; text-transform: uppercase;
  }
  .subhead strong { font-weight: 800; text-decoration: underline; text-underline-offset: 3px; }

  .intro {
    left: 64px; top: 131px; width: 840px;
    font-size: 13.4px; line-height: 20px; font-weight: 400;
  }

  .rules { left: 64px; top: 206px; list-style: none; padding: 0; }
  .rules li { font-size: 33px; line-height: 54.5px; font-weight: 400; }
  .rules strong { font-weight: 800; }

  .brand-name {
    left: 34px; top: 538px;
    font-size: 12px; font-weight: 700; color: var(--brand-violet);
  }

  .report-offer { left: 540px; top: 504px; width: 350px; text-align: center; }
  .report-offer p { margin: 0; font-size: 19px; letter-spacing: 0.5px; line-height: 28px; }
  .report-offer strong { font-weight: 800; }
  .report-offer .web-address { font-size: 27px; letter-spacing: 1.4px; line-height: 34px; }

  .invitation { left: 0; top: 640px; width: 800px; text-align: center; }
  .invitation h2 { margin: 0; font-size: 52px; font-weight: 800; line-height: 66px; }
  .invitation .event-details { margin: 4px 0 0; font-size: 19px; font-weight: 700; }
  .invitation .pitch {
    margin: 36px 0 0; font-size: 19.5px; font-style: italic; line-height: 28px;
  }
</style>
</head>
<body>
<main class="postcard">
  <svg class="swoosh-band" viewBox="0 0 927 600" aria-hidden="true">
    <defs>
      <linearGradient id="mintFade" x1="0" y1="0" x2="0" y2="1">
        <stop offset="0" stop-color="var(--mint)"/>
        <stop offset="0.8" stop-color="var(--mint)"/>
        <stop offset="1" stop-color="var(--mint-pale)"/>
      </linearGradient>
    </defs>
    <path d="M0,420 C300,478 760,478 927,262 L927,600 L0,600 Z" fill="var(--coral)"/>
    <path d="M0,442 C300,495 800,485 927,295 L927,600 L0,600 Z" fill="url(#mintFade)"/>
  </svg>

  <h1 class="headline">Climb the <strong>MARLOW</strong></h1>
  <p class="subhead">Get out of debt <strong>before</strong> you retire!</p>
  <p class="intro">Think about this... Most financial firms are more concerned about you rolling your retirement assets over to them than they are about helping you with real solutions to real problems.<br>We believe the four most important rules for retirement are:</p>

  <ul class="rules">
    <li>Have <strong>MARLOW</strong> debt.</li>
    <li>Pay <strong>MARLOW</strong> taxes.</li>
    <li>Take <strong>MARLOW</strong> risk.</li>
    <li>Have <strong>MARLOW</strong> worries.</li>
  </ul>

  <p class="brand-name">The Brenwick Group, LLC</p>

  <div class="report-offer">
    <p>For your <strong>FREE</strong> report, go to</p>
    <p class="web-address">www.MarlowPathway.com</p>
  </div>

  <section class="invitation">
    <h2>YOUR INVITED!</h2>
    <p class="event-details">To our workshop (TIME), (DATE), (PLACE)</p>
    <p class="pitch">Let us help you take a different, and we believe better, approach to<br>planning your retirement.</p>
  </section>
</main>
</body>
</html>
```